Unique business card design

Boutique coastal hotel suites - in need of clever stand out business card I have uploaded the logo that I had created through brand loft I want something that is clever and stands out from everyone else - 418 Marrowind Lane seldovia Alaska 99528 phone or text 907 -561-8204 www.tidewrenlodgeinn.com

Target Market(s)

Men and woman

Industry/Entity Type

Boutique coastal hotel

Contact Information for Business Card

Tidewren Lodge Kelpwater Alaska tidewren_lodge@kelpmail.com

Requirements
Must have
• Classy - clever -bold 907-561-8204 call or text

```html
<!DOCTYPE html>
<html lang="en">
<head>
<meta charset="utf-8">
<title>Tidewren Lodge — Business Card</title>
<link href="https://fonts.googleapis.com/css2?family=Poppins:wght@300;400;600;700&display=swap" rel="stylesheet">
<style>
  :root {
    --backdrop: #e4e5e7;
    --navy: #2b4a63;
    --deep-teal: #114d5e;
    --signal-red: #c1212b;
    --card-white: #f3f3f2;
    --panel-sand: #e7e4dc;
    --ink: #3a3d42;
    --rule: #3f5c75;
  }
  * { margin: 0; padding: 0; box-sizing: border-box; }
  html, body { width: 1200px; height: 944px; overflow: hidden; }
  body {
    background: var(--backdrop);
    font-family: "Poppins", sans-serif;
    position: relative;
  }
  .card {
    position: absolute;
    left: 250px;
    width: 700px;
    height: 400px;
    box-shadow: 0 6px 18px rgba(0,0,0,0.12);
    overflow: hidden;
  }
  .card--front { top: 50px; background: var(--navy); }
  .card--back { top: 494px; background: var(--card-white); }

  .brand-panel {
    position: absolute;
    background: var(--panel-sand);
    display: flex;
    align-items: center;
    justify-content: center;
    gap: 12px;
  }
  .card--front .brand-panel { left: 205px; top: 145px; width: 290px; height: 110px; }
  .card--back .brand-panel { left: 410px; top: 42px; width: 240px; height: 90px; }
  .brand-mark { width: 16px; height: 16px; background: var(--signal-red); }
  .brand-name {
    font-weight: 600;
    color: var(--navy);
    letter-spacing: 0.04em;
    text-transform: uppercase;
  }
  .card--front .brand-name { font-size: 25px; }
  .card--back .brand-name { font-size: 20px; }

  .divider-rule {
    position: absolute;
    left: 350px;
    top: 180px;
    width: 300px;
    height: 1px;
    background: var(--rule);
  }
  .holder {
    position: absolute;
    left: 120px;
    top: 150px;
  }
  .holder-name {
    font-size: 26px;
    font-weight: 700;
    letter-spacing: 0.01em;
    color: var(--deep-teal);
    line-height: 1.1;
  }
  .holder-name .surname { color: var(--signal-red); }
  .holder-title {
    font-size: 13px;
    font-weight: 300;
    color: var(--ink);
    margin-top: 2px;
  }
  .contact-list {
    list-style: none;
    margin-top: 14px;
  }
  .contact-list li {
    display: flex;
    align-items: center;
    gap: 9px;
    font-size: 13px;
    font-weight: 300;
    color: var(--ink);
    line-height: 22px;
  }
  .contact-list svg { width: 12px; height: 12px; flex: none; }
  .address {
    position: absolute;
    right: 50px;
    top: 205px;
    text-align: right;
    font-size: 13px;
    font-weight: 300;
    color: var(--ink);
    line-height: 19px;
    font-style: normal;
  }
  .footer-band {
    position: absolute;
    left: 0;
    bottom: 42px;
    width: 100%;
    height: 11px;
    display: flex;
  }
  .footer-band .band-navy { width: 68%; background: var(--navy); }
  .footer-band .band-red { flex: 1; background: var(--signal-red); }
</style>
</head>
<body>

<section class="card card--front" aria-label="Card front">
  <div class="brand-panel">
    <span class="brand-mark"></span>
    <span class="brand-name">Tidewren Lodge</span>
  </div>
</section>

<section class="card card--back" aria-label="Card back">
  <div class="brand-panel">
    <span class="brand-mark"></span>
    <span class="brand-name">Tidewren Lodge</span>
  </div>
  <div class="divider-rule"></div>

  <div class="holder">
    <h1 class="holder-name">DORIAN <span class="surname">HALVIK</span></h1>
    <p class="holder-title">CEO &amp; Founder</p>
    <ul class="contact-list">
      <li>
        <svg viewBox="0 0 12 12" aria-hidden="true"><circle cx="6" cy="6" r="6" fill="#c1212b"/><path d="M3.8 3.2l1 .2.4 1.3-.6.6a4 4 0 0 0 2.1 2.1l.6-.6 1.3.4.2 1-.8.6C5.6 8.6 3.4 6.4 3.2 4z" fill="#fff"/></svg>
        907 -561-8204
      </li>
      <li>
        <svg viewBox="0 0 12 12" aria-hidden="true"><rect x="0.5" y="2" width="11" height="8" rx="1" fill="#c1212b"/><path d="M1 2.8l5 3.6 5-3.6" stroke="#fff" stroke-width="1" fill="none"/></svg>
        info@tidewrenlodgeinn.com
      </li>
      <li>
        <svg viewBox="0 0 12 12" aria-hidden="true"><circle cx="6" cy="6" r="6" fill="#c1212b"/><path d="M1 6h10M6 0.5c-2 2-2 9 0 11M6 0.5c2 2 2 9 0 11" stroke="#fff" stroke-width="0.8" fill="none"/></svg>
        www.tidewrenlodgeinn.com
      </li>
    </ul>
  </div>

  <address class="address">
    418 Marrowind Lane Kelpwater<br>
    Alaska 99528
  </address>

  <div class="footer-band">
    <span class="band-navy"></span>
    <span class="band-red"></span>
  </div>
</section>

</body>
</html>
```